Packaging for Cellphone and tablet case
Need Professional Design
We need packaging for leather case for tablets and cellphones. Minimal design and content. at least 60% transparent area to make product visible from front and back.
Incorporate our logo, packaging colors, Black, grey and white.
Electronics
General audience
Must provide PSD or AI file, Resolution of 300 PPI.
LoGo AI File
This is the sample package that was designed initially,
We would like to have same amount of content on the back and front side of the package.
Sample leather.
Screen Protector packaging that we use.

```html
<!DOCTYPE html>
<html lang="en">
<head>
<meta charset="utf-8">
<title>Corvane Executive Style Case – Packaging Dieline</title>
<link rel="stylesheet" href="https://fonts.googleapis.com/css2?family=Montserrat:wght@600&family=Cormorant+Garamond:ital,wght@1,600&display=swap">
<style>
  :root {
    --stage: #6c6c6c;
    --box-black: #151515;
    --box-black-soft: #1f1f1f;
    --window: #ffffff;
    --tab-grey: #5a5a5a;
    --tab-grey-light: #8a8a8a;
    --fold-line: #9a9a9a;
    --text-white: #f2f2f2;
    --text-grey: #a8a8a8;
  }
  html, body {
    margin: 0;
    width: 1200px;
    height: 780px;
    overflow: hidden;
    background: var(--stage);
  }
  .dieline { display: block; width: 1200px; height: 780px; }
  .box-body { fill: var(--box-black); }
  .tuck-flap { fill: var(--box-black-soft); stroke: var(--fold-line); stroke-width: 0.4; stroke-dasharray: 1.5 1.2; }
  .hang-tab { fill: var(--tab-grey); }
  .hang-tab--front { fill: var(--tab-grey-light); opacity: .55; }
  .hang-slot { fill: var(--tab-grey-light); }
  .fold-line { stroke: var(--fold-line); stroke-width: 0.4; stroke-dasharray: 1.5 1.2; fill: none; }
  .product-window { fill: var(--window); }
  .brand-mark { fill: var(--text-white); }
  .brand-name { font-family: "Montserrat", sans-serif; font-weight: 600; fill: var(--text-white); font-size: 4.2px; letter-spacing: .5px; }
  .product-title { font-family: "Cormorant Garamond", serif; font-style: italic; font-weight: 600; fill: var(--text-white); font-size: 7px; }
  .fine-print { font-family: "Montserrat", sans-serif; font-weight: 600; fill: var(--text-grey); font-size: 1.4px; }
  .feature-icon { fill: none; stroke: var(--text-white); stroke-width: .5; }
  .spec-box { fill: none; stroke: var(--text-grey); stroke-width: .4; }
  .flow-lines { opacity: .6; }
</style>
</head>
<body>
<svg class="dieline" viewBox="-25 34 400 260" xmlns="http://www.w3.org/2000/svg">
  <defs>
    <linearGradient id="flowTone" x1="0" y1="0" x2="1" y2="1">
      <stop offset="0" stop-color="#151515"/>
      <stop offset=".5" stop-color="#4a4a4a"/>
      <stop offset="1" stop-color="#151515"/>
    </linearGradient>
  </defs>

  <!-- top tuck flap and hang tabs -->
  <path class="tuck-flap" d="M35 65 V60 Q35 55 40 55 H118 Q123 55 123 60 V65 Z"/>
  <g class="hang-tab-back">
    <path class="hang-tab" d="M243 66 V45 Q243 42 246 42 H272 Q275 42 275 45 V66 Z"/>
    <rect class="hang-slot" x="252" y="46" width="14" height="3" rx="1.5"/>
    <rect class="hang-slot" x="252" y="58" width="14" height="3" rx="1.5"/>
    <line class="fold-line" x1="243" y1="54" x2="275" y2="54"/>
  </g>

  <!-- main panels -->
  <rect class="box-body" x="12" y="65" width="325" height="230"/>
  <rect class="hang-tab hang-tab--front" x="96" y="65" width="26" height="10"/>
  <line class="fold-line" x1="32" y1="65" x2="32" y2="295"/>
  <line class="fold-line" x1="12" y1="65" x2="337" y2="65"/>
  <line class="fold-line" x1="180" y1="65" x2="180" y2="93"/>
  <line class="fold-line" x1="180" y1="255" x2="180" y2="295"/>

  <!-- decorative flowing line areas -->
  <rect class="flow-lines" x="150" y="72" width="50" height="40" fill="url(#flowTone)" role="img" aria-label="Flowing white line decoration"/>
  <rect class="flow-lines" x="295" y="80" width="40" height="170" fill="url(#flowTone)" role="img" aria-label="Flowing white line decoration"/>

  <!-- transparent product window -->
  <path class="product-window" d="M56 93 H221 Q225 93 227 96 L229 99 Q230 101 233 101 H320 Q326 101 326 107 V230 Q326 236 320 240 Q312 246 306 255 H56 Q50 255 50 249 V99 Q50 93 56 93 Z"/>

  <!-- front branding -->
  <g class="front-brand">
    <rect class="brand-mark" x="87" y="74" width="4" height="4"/>
    <text class="brand-name" x="89" y="83.5" text-anchor="middle">CORVANE</text>
  </g>
  <text class="product-title" x="74" y="273">Executive Sytle Case</text>
  <text class="fine-print" x="95" y="279" text-anchor="middle">www.corvane-cases.com</text>

  <!-- back features -->
  <g class="feature-list">
    <rect class="feature-icon" x="204" y="259" width="6" height="6" rx="1"/>
    <text class="fine-print" x="207" y="268" text-anchor="middle">Slim fit</text>
    <rect class="feature-icon" x="218" y="259" width="6" height="6" rx="1"/>
    <text class="fine-print" x="221" y="268" text-anchor="middle">Soft lining</text>
    <rect class="feature-icon" x="232" y="259" width="6" height="6" rx="1"/>
    <text class="fine-print" x="235" y="268" text-anchor="middle">Easy access</text>
  </g>
  <g class="spec-panel">
    <rect class="spec-box" x="250" y="258" width="30" height="9"/>
    <text class="fine-print" x="265" y="261" text-anchor="middle">Model CV-201</text>
    <circle class="feature-icon" cx="258" cy="264" r="1.3"/>
    <rect class="feature-icon" x="266" y="262.8" width="7" height="2.4" rx="1"/>
  </g>
  <g class="back-brand">
    <rect class="brand-mark" x="258" y="271.5" width="2.5" height="2.5"/>
    <text class="brand-name" x="262" y="274" style="font-size:3px">CORVANE</text>
  </g>
  <text class="fine-print" x="265" y="280" text-anchor="middle">Designed by Corvane Ltd, all rights reserved</text>
</svg>
</body>
</html>
```